Casa Morellina Togo Menu seperated in categories

new to go menu for italian restaurant with menu descriptions and prices i like the cover first page to have all the restaurant information, the other pages should be separated in the menu categories, and if we can include a map with the location of the restaurant
Casa Morellina
42 Route 58 S
North Myrtle Beach, SC 29582
open 7 days a week 4-10
Happy hour served Daily at the Bar 4-7
www.casamorellina.com
casamorellinadk@brivomail.com

Sans Serif

• Prices and pictures and restaurant information

```html
<!DOCTYPE html>
<html lang="en">
<head>
<meta charset="utf-8">
<title>Casa Morellina – Pollo &amp; Vitello</title>
<link rel="stylesheet" href="https://fonts.googleapis.com/css2?family=Open+Sans:wght@400&family=Stint+Ultra+Condensed&family=Antonio:wght@500&display=swap">
<style>
  :root {
    --paper: #ffffff;
    --ink: #1c1c1c;
    --accent: #a3222b;
    --frame: #9b2a2e;
    --sauce: #c8602f;
    --cheese: #efe2c6;
    --plate: #e9e9ea;
    --grill: #3a2720;
  }
  * { margin: 0; padding: 0; box-sizing: border-box; }
  html, body { width: 667px; height: 1200px; overflow: hidden; background: var(--paper); }
  .menu-page {
    position: relative; width: 667px; height: 1200px;
    font-family: "Open Sans", Arial, sans-serif; color: var(--ink);
  }
  .frame {
    position: absolute; left: 40px; top: 40px; width: 588px; height: 1121px;
    border: 2px solid var(--frame);
  }
  .title {
    position: absolute; left: 68px; top: 88px;
    font-family: "Stint Ultra Condensed", "Arial Narrow", serif;
    font-size: 94px; line-height: 1; letter-spacing: 1px; color: #111;
  }
  .intro {
    position: absolute; left: 70px; top: 181px; width: 530px;
    font-size: 14px; line-height: 18px;
  }
  .addon {
    position: absolute; font-size: 11px; line-height: 13px;
  }
  .addon .price { font-family: "Antonio", "Arial Narrow", sans-serif; color: var(--accent); font-size: 15px; margin-left: 6px; }
  .addon-caesar { left: 238px; top: 245px; }
  .addon-split { left: 424px; top: 234px; display: flex; align-items: flex-end; }
  .addon-split .price { margin-left: 14px; }
  .dish { position: absolute; width: 250px; }
  .dish-name {
    font-family: "Stint Ultra Condensed", "Arial Narrow", serif;
    font-size: 23px; line-height: 22px; color: #111;
  }
  .dish-desc { font-size: 14px; line-height: 18px; margin-bottom: 5px; }
  .price-row { display: flex; align-items: center; height: 26px; font-size: 14px; }
  .price-row .label { flex: none; }
  .price-row .leader {
    flex: 1; height: 0; border-bottom: 1.5px dashed var(--accent);
    margin: 4px 8px 0 6px;
  }
  .price-row .amount {
    flex: none; width: 44px;
    font-family: "Antonio", "Arial Narrow", sans-serif; font-weight: 500;
    font-size: 22px; color: var(--accent);
  }
  .col-left { left: 55px; width: 194px; }
  .col-left .dish-desc { width: 250px; }
  .col-right { left: 366px; width: 194px; }
  .col-right .dish-desc { width: 230px; }
  .photo { position: absolute; }
  .photo-parmigiana { left: 345px; top: 843px; width: 282px; height: 125px;
    background: linear-gradient(100deg, var(--sauce) 0%, #d7854c 45%, var(--cheese) 70%, #f3ead5 100%); }
  .photo-shank { left: 345px; top: 970px; width: 282px; height: 190px;
    background: radial-gradient(ellipse at 45% 50%, #a8442a 0%, #d89a5a 30%, #f0f0f0 65%, #dcdcdc 100%); }
  .photo-medallions { left: 40px; top: 1017px; width: 300px; height: 143px;
    background: radial-gradient(ellipse at 45% 50%, var(--grill) 0%, #5a4036 40%, var(--plate) 80%); }
</style>
</head>
<body>
<main class="menu-page">
  <div class="frame"></div>

  <h1 class="title">POLLO &amp; VITELLO</h1>
  <p class="intro">All of our Chicken &amp; Veal Dishes served with fresh baked bread and our roasted red pepper, garlic and herb dipping oil, your choice of soup of the day or house salad</p>
  <p class="addon addon-caesar">Upgrade to Caesar Salad<span class="price">1.95</span></p>
  <p class="addon addon-split"><span>Split Entrée includes<br>additional soup or salad</span><span class="price">7.00</span></p>

  <section class="dish col-left" style="top:310px">
    <h2 class="dish-name">Parmigiana</h2>
    <p class="dish-desc">Hand breaded, lightly fried, and topped with our Marinara sauce and fresh Mozzarella, baked to perfection, served over spaghetti</p>
    <div class="price-row"><span class="label">Eggplant</span><span class="leader"></span><span class="amount">15.95</span></div>
    <div class="price-row"><span class="label">Chicken</span><span class="leader"></span><span class="amount">18.95</span></div>
    <div class="price-row"><span class="label">Veal</span><span class="leader"></span><span class="amount">20.95</span></div>
  </section>

  <section class="dish col-right" style="top:310px">
    <h2 class="dish-name">Picatta</h2>
    <p class="dish-desc">Sautéed in a chardonnay lemon butter sauce with Capers, Artichoke hearts and Garlic, served over penne pasta</p>
    <div class="price-row"><span class="label">Chicken</span><span class="leader"></span><span class="amount">18.95</span></div>
    <div class="price-row"><span class="label">Veal</span><span class="leader"></span><span class="amount">21.95</span></div>
  </section>

  <section class="dish col-left" style="top:507px">
    <h2 class="dish-name">Marsala</h2>
    <p class="dish-desc">Sautéed with Mushrooms in a fine Sicilian dry Marsala wine, served over penne pasta</p>
    <div class="price-row"><span class="label">Chicken</span><span class="leader"></span><span class="amount">18.95</span></div>
    <div class="price-row"><span class="label">Veal</span><span class="leader"></span><span class="amount">21.95</span></div>
  </section>

  <section class="dish col-right" style="top:507px">
    <h2 class="dish-name">Francaise</h2>
    <p class="dish-desc">Egg battered finished in a lemon chardonnay butter sauce, served over penne pasta</p>
    <div class="price-row"><span class="label">Chicken</span><span class="leader"></span><span class="amount">18.95</span></div>
    <div class="price-row"><span class="label">Veal</span><span class="leader"></span><span class="amount">21.95</span></div>
  </section>

  <section class="dish col-left" style="top:671px">
    <h2 class="dish-name">Saltimbocca</h2>
    <p class="dish-desc">Prosciutto topped with Ricotta and Mozzarella cheese, in a Marsala demi-glaze sauce, served over sautéed spinach and penne pasta</p>
    <div class="price-row"><span class="label">Chicken</span><span class="leader"></span><span class="amount">20.95</span></div>
    <div class="price-row"><span class="label">Veal</span><span class="leader"></span><span class="amount">22.95</span></div>
  </section>

  <section class="dish col-right" style="top:671px">
    <h2 class="dish-name">Margarita</h2>
    <p class="dish-desc">Sautéed with Sundried Tomatoes, roasted Garlic in a creamy balsamic reduction sauce, topped with fresh Mozzarella cheese, served over penne pasta</p>
    <div class="price-row"><span class="label">Chicken</span><span class="leader"></span><span class="amount">20.95</span></div>
    <div class="price-row"><span class="label">Veal</span><span class="leader"></span><span class="amount">22.95</span></div>
  </section>

  <section class="dish col-left" style="top:838px">
    <h2 class="dish-name">Sorrento</h2>
    <p class="dish-desc">Prosciutto topped with Eggplant, Roasted Red Peppers, Mushrooms, Ricotta and fresh Mozzarella cheese in a creamy Tomato sauce served over penne pasta</p>
    <div class="price-row"><span class="label">Chicken</span><span class="leader"></span><span class="amount">20.95</span></div>
    <div class="price-row"><span class="label">Veal</span><span class="leader"></span><span class="amount">22.95</span></div>
  </section>

  <div class="photo photo-parmigiana" role="img" aria-label="Photo of chicken parmigiana with penne pasta in tomato sauce"></div>
  <div class="photo photo-shank" role="img" aria-label="Photo of braised veal in red sauce over risotto with crispy fried vegetables"></div>
  <div class="photo photo-medallions" role="img" aria-label="Photo of grilled veal medallions drizzled with balsamic glaze on a white plate"></div>
</main>
</body>
</html>
```